Copperleaf Motorized Shade Business Card

Hello, we've had our logo made. Now we are looking for a clean and cool looking business card. One side can just be the logo with any design elements that might look good with it. The other side will be Name, Phone Number and Email. There will not be an address on the card.

```html
<!DOCTYPE html>
<html lang="en">
<head>
<meta charset="utf-8">
<title>Copperleaf Motorized Shade – Business Card</title>
<link rel="stylesheet" href="https://fonts.googleapis.com/css2?family=Fira+Sans:wght@400;600;700&display=swap">
<style>
  :root {
    --backdrop: #9a9a9a;
    --navy: #003a78;
    --navy-deep: #002d63;
    --sky: #00a8e8;
    --sun: #f7c21b;
    --card-light: #e4e4e4;
    --ink-grey: #4a4a4a;
    --white: #ffffff;
  }
  * { margin: 0; padding: 0; box-sizing: border-box; }
  html, body {
    width: 1200px; height: 900px; overflow: hidden;
    background: var(--backdrop);
    font-family: "Fira Sans", sans-serif;
  }
  .card {
    position: absolute;
    left: 363px;
    width: 474px; height: 271px;
    border-radius: 14px;
    overflow: hidden;
  }
  .card--front { top: 145px; background: var(--navy); }
  .card--back { top: 484px; background: var(--card-light); }

  .front-texture {
    position: absolute; left: 0; top: 0;
    width: 205px; height: 271px;
    background: linear-gradient(90deg, #00336c 0%, #003a78 100%);
    opacity: 0.9;
  }
  .wordmark {
    position: absolute;
    display: flex; align-items: center; gap: 10px;
    font-weight: 600;
    line-height: 1.05;
  }
  .wordmark__dot {
    width: 18px; height: 18px; border-radius: 50%;
    background: var(--sun);
    flex: none;
  }
  .wordmark__name { font-size: 25px; }
  .card--front .wordmark { left: 268px; top: 108px; color: var(--white); }
  .card--back .wordmark { left: 282px; top: 80px; color: var(--navy); }

  .contact-block { position: absolute; left: 26px; top: 50px; }
  .person-name {
    font-size: 13px; font-weight: 700; letter-spacing: 0.3px;
    color: var(--navy); text-transform: uppercase;
  }
  .person-title { font-size: 11px; color: var(--ink-grey); margin-top: 2px; }
  .divider {
    width: 17px; height: 1.5px; background: var(--sky);
    margin: 16px 0 20px;
  }
  .contact-list { list-style: none; }
  .contact-list li {
    display: flex; align-items: center; gap: 5px;
    font-size: 10.5px; color: var(--ink-grey);
    height: 15px;
  }
  .contact-icon { width: 13px; height: 13px; flex: none; }
  .wave { position: absolute; left: 0; bottom: 0; width: 474px; height: 271px; }
</style>
</head>
<body>
  <section class="card card--front" aria-label="Card front">
    <div class="front-texture" role="img" aria-label="Faint window shade texture in navy tones"></div>
    <div class="wordmark">
      <span class="wordmark__dot"></span>
      <span class="wordmark__name">Copperleaf<br>Motorized Shade</span>
    </div>
  </section>

  <section class="card card--back" aria-label="Card back">
    <div class="contact-block">
      <p class="person-name">Marcus Hale</p>
      <p class="person-title">President/Owner</p>
      <div class="divider"></div>
      <ul class="contact-list">
        <li>
          <svg class="contact-icon" viewBox="0 0 14 14" aria-hidden="true">
            <circle cx="7" cy="7" r="6.2" fill="none" stroke="var(--sun)" stroke-width="1.2"/>
            <path d="M4.6 3.8c.4-.3.8-.3 1 .1l.6 1.1c.2.3.1.6-.2.8l-.4.3c.4.9 1 1.5 1.9 1.9l.3-.4c.2-.3.5-.4.8-.2l1.1.6c.4.2.4.6.1 1l-.5.5c-.4.4-1 .5-1.6.2C6 9 5 8 4.3 6.4c-.3-.6-.2-1.2.2-1.6z" fill="var(--navy)"/>
          </svg>
          555.214.0397
        </li>
        <li>
          <svg class="contact-icon" viewBox="0 0 14 14" aria-hidden="true">
            <circle cx="7" cy="7" r="6.2" fill="none" stroke="var(--sun)" stroke-width="1.2"/>
            <rect x="3.8" y="4.8" width="6.4" height="4.4" fill="var(--navy)"/>
            <path d="M3.9 4.9 7 7.3l3.1-2.4" fill="none" stroke="var(--card-light)" stroke-width="0.7"/>
          </svg>
          info@copperleafshades.com
        </li>
        <li>
          <svg class="contact-icon" viewBox="0 0 14 14" aria-hidden="true">
            <circle cx="7" cy="7" r="6.2" fill="none" stroke="var(--sun)" stroke-width="1.2"/>
            <circle cx="7" cy="7" r="3.6" fill="var(--navy)"/>
            <path d="M3.4 7h7.2M7 3.4v7.2M4.1 5.3h5.8M4.1 8.7h5.8" stroke="var(--card-light)" stroke-width="0.5" fill="none"/>
          </svg>
          www.copperleafshades.com
        </li>
      </ul>
    </div>

    <div class="wordmark">
      <span class="wordmark__dot"></span>
      <span class="wordmark__name">Copperleaf<br>Motorized Shade</span>
    </div>

    <svg class="wave" viewBox="0 0 790 451" preserveAspectRatio="none" aria-hidden="true">
      <path d="M0 358 C150 430 330 418 500 378 C640 345 720 335 790 358 L790 451 L0 451 Z" fill="var(--navy-deep)"/>
      <path d="M0 372 C150 440 330 425 500 385 C640 352 720 345 790 368 L790 451 L0 451 Z" fill="var(--sky)"/>
      <path d="M0 395 C160 455 330 440 500 400 C640 368 720 360 790 395 L790 451 L0 451 Z" fill="var(--navy-deep)"/>
      <path d="M0 408 C170 462 340 445 510 405 C640 375 720 372 790 420 L790 451 L0 451 Z" fill="var(--navy)"/>
    </svg>
  </section>
</body>
</html>
```